Re-Branding

I would like a new "brand" which will incorporate my new photo. I do title insurance in California for Harborline Deed Assurance Corp. Could be used on business cards or flyers.

Target Market(s)

Real Estate Professionals, Attorneys, Mortgage Companies and Banks.

Contact Information for Business Card

High Gloss

Requirements
Must have
• My photo, my logo and my contact information.
Nice to have
• background that is appealing to clients
Should not have
• home email address

```html
<!DOCTYPE html>
<html lang="en">
<head>
<meta charset="utf-8">
<title>Dana Whitfield — Business Card</title>
<link href="https://fonts.googleapis.com/css2?family=Libre+Baskerville:wght@400;700&display=swap" rel="stylesheet">
<style>
  :root {
    --page-bg: #2b2b2b;
    --card-black: #141414;
    --card-charcoal: #262626;
    --ink-white: #f4f4f4;
    --ink-soft: #cfcfcf;
    --logo-plate: #e9e9e9;
    --logo-ink: #1f3f7a;
    --photo-light: #9a9a9a;
    --photo-dark: #3a3a3a;
  }
  * { box-sizing: border-box; margin: 0; padding: 0; }
  html, body {
    width: 1200px; height: 900px; overflow: hidden;
    background: var(--page-bg);
    font-family: "Libre Baskerville", "Times New Roman", serif;
    color: var(--ink-white);
  }
  .canvas {
    width: 1200px; height: 900px;
    display: flex; flex-direction: column; align-items: center; justify-content: center;
    gap: 40px;
  }
  .card {
    position: relative;
    width: 660px; height: 377px;
    border-radius: 14px;
    overflow: hidden;
    background: linear-gradient(135deg, var(--card-charcoal) 0%, var(--card-black) 55%, var(--card-charcoal) 100%);
    box-shadow: 0 10px 30px rgba(0,0,0,.45);
  }

  /* Back of card */
  .card-back .contact-block {
    position: absolute; top: 92px; left: 0; right: 0;
    text-align: center;
  }
  .card-back .website {
    font-size: 17px; letter-spacing: 5px; font-weight: 700;
  }
  .card-back .phone {
    font-size: 50px; letter-spacing: 1px; margin-top: 6px; line-height: 1.1;
  }
  .card-back .email {
    font-size: 22px; margin-top: 6px; color: var(--ink-soft);
  }
  .card-back .footer-links {
    position: absolute; bottom: 38px; left: 0; right: 0;
    text-align: center; font-size: 12px; font-weight: 700; color: var(--ink-soft);
  }
  .card-back .divider { margin: 0 10px; }

  /* Front of card */
  .card-front .portrait {
    position: absolute; top: 0; right: 0;
    width: 300px; height: 310px;
    background: radial-gradient(ellipse at 45% 35%, var(--photo-light) 0%, #6c6c6c 45%, var(--photo-dark) 100%);
  }
  .card-front .identity {
    position: absolute; left: 92px; top: 205px;
  }
  .card-front .name {
    font-size: 40px; font-weight: 400; letter-spacing: .5px; line-height: 1.1;
  }
  .card-front .role {
    font-size: 14px; color: var(--ink-soft); margin-top: 6px;
  }
  .card-front .logo-plate {
    position: absolute; left: 260px; bottom: 12px;
    width: 340px; height: 46px;
    background: var(--logo-plate);
    border-radius: 8px;
    display: flex; align-items: center; gap: 9px;
    padding: 0 14px;
  }
  .card-front .logo-mark {
    width: 16px; height: 16px; background: var(--logo-ink); flex: none;
  }
  .card-front .logo-name {
    font-size: 13px; color: var(--logo-ink); white-space: nowrap;
  }
</style>
</head>
<body>
  <main class="canvas">
    <section class="card card-back" aria-label="Card back">
      <div class="contact-block">
        <p class="website">www.Dana.harborlineIE.com</p>
        <p class="phone">909-555-0182</p>
        <p class="email">DWhitfield@hdac.com</p>
      </div>
      <p class="footer-links">www.HarborlineAgent.com<span class="divider">|</span>DeedTalk.com/Connect</p>
    </section>

    <section class="card card-front" aria-label="Card front">
      <div class="portrait" role="img" aria-label="Black and white portrait photo of the account executive"></div>
      <div class="identity">
        <h1 class="name">Dana Whitfield</h1>
        <p class="role">Account Executive | Vice President</p>
      </div>
      <div class="logo-plate">
        <span class="logo-mark"></span>
        <span class="logo-name">Harborline Deed Assurance Corp.</span>
      </div>
    </section>
  </main>
</body>
</html>
```